Business Card and Letterhead for Nurlo - modern real estate business

I need a double sided business card design for Nurlo. Please see business card brief here https://papers.trelvimo.net/sheet/q/7XrTbaLeZpMmQ2uWvd9HkCj4yNoEfsGi3lRtAz_pk/view?mode=shared

Please feel free to design the business cards however you feel best. I am happy to give some creative freedoms and then provide feedback from there.

Please then also create a letterhead to match the business card design

Colors

Designer to choose colors to be used in the design.

Requirements
Must have
• Must be a modern, elegant business card which looks very professional

```html
<!DOCTYPE html>
<html lang="en">
<head>
<meta charset="utf-8">
<title>Nurlo – Business Card</title>
<link href="https://fonts.googleapis.com/css2?family=Roboto:wght@400;500;700&display=swap" rel="stylesheet">
<style>
  :root {
    --stage: #2b2b2d;
    --card-dark: #262628;
    --card-light: #ffffff;
    --brand-red: #e3101f;
    --silver: #cfd1d4;
    --ink: #333333;
    --photo-top: #c9d3cf;
    --photo-bottom: #6f7b74;
  }
  * { box-sizing: border-box; margin: 0; padding: 0; }
  html, body { width: 1200px; height: 960px; overflow: hidden; }
  body {
    background: var(--stage);
    font-family: 'Roboto', Arial, sans-serif;
    position: relative;
  }
  .card {
    position: absolute;
    width: 620px;
    height: 354px;
    left: 290px;
    border-bottom: 4px solid var(--brand-red);
    border-left: 2px solid var(--brand-red);
  }
  .card--back {
    top: 70px;
    background: var(--card-dark);
    display: flex;
    align-items: center;
    justify-content: center;
  }
  .card--front {
    top: 500px;
    background: var(--card-light);
  }
  .wordmark {
    font-weight: 700;
    letter-spacing: 4px;
    line-height: 1;
    text-transform: uppercase;
  }
  .card--back .wordmark {
    color: var(--silver);
    font-size: 78px;
    transform: translateX(30px);
  }
  .card--front .wordmark {
    position: absolute;
    left: 70px;
    top: 120px;
    color: var(--brand-red);
    font-size: 72px;
  }
  .portrait {
    position: absolute;
    right: 70px;
    top: 28px;
    width: 150px;
    height: 112px;
    border: 1px solid #555;
    background: linear-gradient(160deg, var(--photo-top), var(--photo-bottom));
  }
  .name-band {
    position: absolute;
    right: 0;
    top: 228px;
    width: 270px;
    height: 62px;
    background: var(--brand-red);
    border-left: 3px solid #1a1a1a;
    border-bottom: 3px solid #1a1a1a;
    color: #fff;
    text-align: right;
    padding: 9px 18px 0 0;
  }
  .name-band__name { font-size: 20px; font-weight: 700; }
  .name-band__title { font-size: 13px; font-weight: 500; margin-top: 2px; }
  .contact {
    position: absolute;
    left: 70px;
    top: 236px;
    color: var(--ink);
    font-size: 14px;
    line-height: 1.3;
  }
  .contact__address { margin-bottom: 10px; }
  .contact__row { display: flex; align-items: center; gap: 8px; }
  .contact__icon { width: 11px; height: 11px; fill: var(--brand-red); flex: none; }
</style>
</head>
<body>
  <section class="card card--back">
    <span class="wordmark">Nurlo</span>
  </section>

  <section class="card card--front">
    <span class="wordmark">Nurlo</span>

    <div class="portrait" role="img" aria-label="Portrait photo of the agent"></div>

    <div class="name-band">
      <div class="name-band__name">Liam Carver</div>
      <div class="name-band__title">Licenced Real Estate Agent</div>
    </div>

    <div class="contact">
      <p class="contact__address">PO Box 1184<br>Brenvale NSW 2790</p>
      <p class="contact__row">
        <svg class="contact__icon" viewBox="0 0 24 24" aria-hidden="true"><path d="M6.6 10.8a15.1 15.1 0 0 0 6.6 6.6l2.2-2.2c.3-.3.7-.4 1-.2 1.1.4 2.3.6 3.6.6.6 0 1 .4 1 1V20c0 .6-.4 1-1 1A17 17 0 0 1 3 4c0-.6.4-1 1-1h3.5c.6 0 1 .4 1 1 0 1.3.2 2.5.6 3.6.1.3 0 .7-.2 1z"/></svg>
        0400 318 927
      </p>
      <p class="contact__row">
        <svg class="contact__icon" viewBox="0 0 24 24" aria-hidden="true"><path d="M2 5h20v14H2z M2 5l10 8 10-8" fill="var(--brand-red)" stroke="#fff" stroke-width="1.5"/></svg>
        liam@nurlo.com
      </p>
      <p class="contact__row">
        <svg class="contact__icon" viewBox="0 0 24 24" aria-hidden="true"><circle cx="12" cy="12" r="11"/><path d="M1 12h22M12 1c4 4 4 18 0 22M12 1c-4 4-4 18 0 22" fill="none" stroke="#fff" stroke-width="1.5"/></svg>
        www.nurlo.com
      </p>
    </div>
  </section>
</body>
</html>
```